New Electrical Business Card Design

I would like a new design for my business cards.
i would like the same logo and font but new design
Please see attached files for front and back design.
large image can be used for graphics.
I would like the instagram link incorporated to back of card.
website site address needs to be changed to www.tidemarkelectrical.au
everything else stays as is

```html
<!DOCTYPE html>
<html lang="en">
<head>
<meta charset="utf-8">
<title>Tidemark Electrical &amp; Data – Business Card</title>
<link rel="stylesheet" href="https://fonts.googleapis.com/css2?family=Montserrat:ital,wght@0,800;1,300;1,800&family=Roboto+Condensed:wght@300;400&display=swap">
<style>
  :root {
    --page-bg: #e6e1dc;
    --card-white: #ffffff;
    --card-black: #231f20;
    --ink-dark: #1f1c1d;
    --ink-grey: #6d6e70;
    --brand-green: #138a43;
    --text-white: #ffffff;
  }
  * { margin: 0; padding: 0; box-sizing: border-box; }
  html, body {
    width: 1200px; height: 1200px; overflow: hidden;
    background: var(--page-bg);
  }
  .sheet { position: relative; width: 1200px; height: 1200px; }

  .card {
    position: absolute; top: 480px;
    width: 420px; height: 240px;
  }
  .card--front { left: 157px; background: var(--card-white); box-shadow: 0 0 0 1px rgba(0,0,0,0.05); }
  .card--back { left: 622px; background: var(--card-black); }

  .brand-name {
    position: absolute;
    font-family: "Montserrat", sans-serif;
    font-weight: 800;
    letter-spacing: 0.3px;
    white-space: nowrap;
    line-height: 1;
  }
  .card--front .brand-name {
    left: 29px; top: 102px;
    font-size: 27px; color: var(--ink-dark);
  }
  .card--back .brand-name {
    left: 0; right: 0; top: 98px;
    text-align: center;
    font-size: 50px; color: var(--text-white);
  }

  .social-frame {
    position: absolute; left: 262px; top: 25px;
    width: 60px; height: 57px;
    border: 1.5px solid var(--brand-green); border-radius: 6px;
    display: flex; align-items: flex-end; justify-content: center;
    padding-bottom: 6px;
  }
  .social-frame__label {
    font-family: "Roboto Condensed", sans-serif;
    font-weight: 300; font-size: 4.5px; letter-spacing: 0.2px;
    color: var(--brand-green); white-space: nowrap;
  }

  .services {
    position: absolute; right: 240px; top: 155px;
    text-align: right;
    font-family: "Roboto Condensed", sans-serif;
    font-weight: 300; font-size: 11px; line-height: 12.5px;
    color: var(--ink-grey); white-space: nowrap;
  }
  .divider {
    position: absolute; left: 228px; top: 104px;
    width: 1.2px; height: 76px; background: var(--brand-green);
  }
  .person-name {
    position: absolute; left: 262px; top: 102px;
    font-family: "Montserrat", sans-serif; font-style: italic;
    font-size: 11px; letter-spacing: 0.2px; white-space: nowrap;
  }
  .person-name .first { font-weight: 800; color: var(--brand-green); }
  .person-name .last { font-weight: 300; color: var(--ink-grey); }

  .contact-list {
    position: absolute; left: 262px; top: 126px;
    list-style: none;
    font-family: "Roboto Condensed", sans-serif;
    font-weight: 300; font-size: 11px; color: var(--ink-grey);
  }
  .contact-list li {
    display: flex; align-items: center; height: 14px; white-space: nowrap;
  }
  .contact-list svg { width: 10px; height: 10px; margin-right: 5px; flex: none; }
  .contact-list .accent { color: var(--brand-green); }

  .legal {
    position: absolute; left: 262px; top: 194px;
    font-family: "Roboto Condensed", sans-serif;
    font-weight: 400; font-size: 9px; line-height: 13px;
    color: var(--ink-grey);
  }
</style>
</head>
<body>
<main class="sheet">

  <section class="card card--front" aria-label="Business card front">
    <div class="brand-name">TIDEMARK</div>
    <p class="services">Residential . Commercil . Industrial<br>24hr service</p>
    <div class="divider"></div>

    <div class="social-frame"><span class="social-frame__label">TIDEMARK.ELECTRICAL</span></div>

    <p class="person-name"><span class="first">DANIEL</span> <span class="last">KOWALCZYK</span></p>

    <ul class="contact-list">
      <li>
        <svg viewBox="0 0 12 12" aria-hidden="true"><rect x="3" y="0.8" width="6" height="10.4" rx="1" fill="none" stroke="#6d6e70" stroke-width="1"/><line x1="5.2" y1="9.6" x2="6.8" y2="9.6" stroke="#6d6e70" stroke-width="0.8"/></svg>
        0431 5862
      </li>
      <li>
        <svg viewBox="0 0 12 12" aria-hidden="true"><rect x="0.8" y="2.5" width="10.4" height="7" fill="#6d6e70"/><polyline points="0.8,2.5 6,6.6 11.2,2.5" fill="none" stroke="#fff" stroke-width="0.9"/></svg>
        info@tidemarkelectrical.au
      </li>
      <li>
        <svg viewBox="0 0 12 12" aria-hidden="true"><circle cx="6" cy="6" r="5" fill="#6d6e70"/><ellipse cx="6" cy="6" rx="2.2" ry="5" fill="none" stroke="#fff" stroke-width="0.7"/><line x1="1" y1="6" x2="11" y2="6" stroke="#fff" stroke-width="0.7"/></svg>
        <span>www.<span class="accent">tidemarkelectrical</span>.au</span>
      </li>
      <li>
        <svg viewBox="0 0 12 12" aria-hidden="true"><circle cx="6" cy="6" r="4.6" fill="none" stroke="#6d6e70" stroke-width="1"/></svg>
        tidemark.electrical
      </li>
    </ul>

    <p class="legal">ABN-62 418207<br>Lic number-518346D</p>
  </section>

  <section class="card card--back" aria-label="Business card back">
    <div class="brand-name">TIDEMARK</div>
  </section>

</main>
</body>
</html>
```